KeyHarbor needs a modern business card

We are a modern conveyancing company and we need to appeal to the top (Multi-million dollar properties)and bottom on the property conveyancing market but our sweet spot is the middle of the market. I like professional with a hint of unconventional.

Target Market(s)

As above

Industry/Entity Type

Real Estate

Contact Information for Business Card

Back Of card:
thinking black with the logo and a tag line (I could be wrong about the black)
Tag line - Clear Guidance, Careful Handover

Front of Card:
Marissa Toll (BBus (Finance) LLB)
Licensed Conveyancer
Email: marissa@keyharbor.com.au

Key Harbor
ABN: 48 913 706
Suite 14, Level 3, 9 Calloway Road Lindhurst Park, NSW 2178
Phone: 1300 682 917

Sydney - Melbourne - Brisbane (Perhaps have this along the bottom of the card)

Requirements
Must have
• Sleek, modern and top end appeal (But approachable)
Should not have
• Not too cluttered

```html
<!DOCTYPE html>
<html lang="en">
<head>
<meta charset="utf-8">
<title>KeyHarbor — Business Card</title>
<link rel="stylesheet" href="https://fonts.googleapis.com/css2?family=Arimo:wght@400;700&family=Noto+Serif:wght@700&display=swap">
<style>
  :root {
    --canvas: #ece9e4;
    --white: #ffffff;
    --navy: #23527a;
    --green: #5cb82e;
    --cyan: #22b6e6;
    --black: #050505;
    --ink: #2b2b2b;
    --grey-strip: #e6e6e6;
    --logo-grey: #5a5a5a;
  }
  * { margin: 0; padding: 0; box-sizing: border-box; }
  html, body { width: 1200px; height: 892px; overflow: hidden; }
  body {
    background: var(--canvas);
    font-family: "Arimo", Arial, sans-serif;
    position: relative;
  }
  .card {
    position: absolute;
    left: 320px;
    width: 560px;
    height: 320px;
    overflow: hidden;
    box-shadow: 0 6px 18px rgba(0,0,0,0.18);
  }

  /* Front */
  .card-front { top: 84px; background: var(--white); }
  .front-brand {
    position: absolute; left: 44px; top: 96px;
    width: 190px;
    display: flex; align-items: center; gap: 12px;
  }
  .brand-square { width: 28px; height: 28px; background: var(--navy); flex: none; }
  .brand-name {
    font-weight: 700; font-size: 30px; color: var(--logo-grey);
    letter-spacing: -0.5px;
  }
  .front-divider {
    position: absolute; left: 250px; top: 50px;
    width: 1px; height: 150px; background: #333;
  }
  .front-details { position: absolute; left: 276px; top: 44px; }
  .person-name {
    font-family: "Noto Serif", Georgia, serif;
    font-weight: 700; font-size: 29px; color: var(--green);
    line-height: 1.1;
  }
  .person-cred, .person-role {
    font-size: 15px; color: var(--ink); line-height: 1.3;
  }
  .contact-list { list-style: none; margin-top: 26px; }
  .contact-list li {
    display: flex; align-items: center; gap: 8px;
    font-size: 15px; color: var(--ink); line-height: 1.5;
  }
  .contact-icon { width: 13px; height: 13px; flex: none; }
  .front-band {
    position: absolute; left: 0; right: 0; bottom: 0; height: 52px;
    background: var(--navy);
    border-top: 4px solid var(--green);
    display: flex; align-items: center; justify-content: center;
  }
  .front-band::before {
    content: ""; position: absolute; left: 0; right: 0; top: 0; height: 5px;
    background: var(--white);
  }
  .address {
    color: var(--white); font-size: 15px; letter-spacing: 0.2px; margin-top: 4px;
  }

  /* Back */
  .card-back { top: 488px; background: var(--black); }
  .back-brand {
    position: absolute; left: 0; right: 0; top: 100px;
    display: flex; align-items: center; justify-content: center; gap: 16px;
  }
  .back-brand .brand-square { width: 34px; height: 34px; background: var(--cyan); }
  .back-brand .brand-name { color: var(--white); font-size: 38px; }
  .back-strip {
    position: absolute; left: 0; right: 0; bottom: 0; height: 60px;
    background: var(--grey-strip);
    border-top: 3px solid var(--cyan);
    display: flex; align-items: center; justify-content: center;
  }
  .tagline { font-size: 19px; color: var(--ink); letter-spacing: 0.3px; }
</style>
</head>
<body>
  <section class="card card-front" aria-label="Card front">
    <div class="front-brand">
      <span class="brand-square"></span>
      <span class="brand-name">KeyHarbor</span>
    </div>
    <div class="front-divider"></div>
    <div class="front-details">
      <h1 class="person-name">Marissa Toll</h1>
      <p class="person-cred">(BBus (Finance) LLB)</p>
      <p class="person-role">Licensed Conveyancer</p>
      <ul class="contact-list">
        <li>
          <svg class="contact-icon" viewBox="0 0 13 13" aria-hidden="true">
            <rect width="13" height="13" fill="#23527a"/>
            <path d="M3.5 3 h2 l1 2 -1 1 a5 5 0 0 0 2 2 l1-1 2 1 v2 a1 1 0 0 1-1 1 A7 7 0 0 1 2.5 4 a1 1 0 0 1 1-1z" fill="#fff"/>
          </svg>
          1300 682 917
        </li>
        <li>
          <svg class="contact-icon" viewBox="0 0 13 13" aria-hidden="true">
            <rect width="13" height="13" fill="#23527a"/>
            <rect x="2.5" y="4" width="8" height="5.5" fill="#fff"/>
            <path d="M2.5 4 L6.5 7 L10.5 4" stroke="#23527a" stroke-width="0.9" fill="none"/>
          </svg>
          marissa@keyharbor.com.au
        </li>
      </ul>
    </div>
    <div class="front-band">
      <p class="address">Suite 14, Level 3, 9 Calloway Road Lindhurst Park, NSW 2178</p>
    </div>
  </section>

  <section class="card card-back" aria-label="Card back">
    <div class="back-brand">
      <span class="brand-square"></span>
      <span class="brand-name">KeyHarbor</span>
    </div>
    <div class="back-strip">
      <p class="tagline">Clear Guidance, Careful Handover</p>
    </div>
  </section>
</body>
</html>
```